Website design for commercial and residential security company

we're looking to see some new designs for an established company with no website.

homepage and one inner page

here is a link to the homepage content, sitemap, logo and more.
https://files.brontavel.net/share/7QxmPzLrTw2vNkdJhYcsa9eFgbUoiVwRn?view=open

call to action should be Request A Quote

if you have any questions please send them to us asap

thank you

1 page

Sans Serif

```html
<!DOCTYPE html>
<html lang="en">
<head>
<meta charset="utf-8">
<title>Polaris Guard Solutions — Security for Business and Home</title>
<link rel="stylesheet" href="https://fonts.googleapis.com/css2?family=Poppins:wght@300;400;500;600&family=Arimo:wght@400;700&display=swap">
<style>
:root{
  --gold:#c99a33;
  --gold-dark:#b7892a;
  --ink:#111111;
  --text:#333333;
  --muted:#777777;
  --soft:#f4f4f4;
  --line:#e3e3e3;
  --white:#ffffff;
  --night:#141414;
}
*{box-sizing:border-box;margin:0;padding:0}
html,body{width:1200px;height:3578px;overflow:hidden}
body{position:relative;background:var(--white);font-family:"Poppins",sans-serif;color:var(--text)}
.abs{position:absolute}
a{color:inherit;text-decoration:none}

/* top bar */
.topbar{left:300px;top:0;width:900px;height:38px;background:#ececec;display:flex;align-items:center;font-size:12px;color:var(--ink)}
.topbar span{display:flex;align-items:center;gap:10px;position:absolute}
.header{left:0;top:38px;width:1200px;height:97px}
.brand{left:62px;top:56px;display:flex;align-items:center;gap:10px;font-family:"Poppins",sans-serif;font-weight:600;font-size:24px;color:var(--gold);letter-spacing:1px}
.brand i{display:block;width:18px;height:18px;border-radius:50%;background:var(--gold)}
.nav{left:551px;top:75px;display:flex;gap:30px;font-size:12px;color:#555}
.nav .active{color:var(--gold)}
.quote{left:983px;top:66px;width:155px;height:36px;background:var(--gold);color:var(--white);font-family:"Arimo",sans-serif;font-weight:700;font-size:14px;display:flex;align-items:center;justify-content:center;box-shadow:2px 2px 0 #ddd}

/* hero */
.hero{left:0;top:135px;width:1200px;height:675px;background:linear-gradient(90deg,#5d5d5c 0%,#8e8d8b 40%,#c9c8c4 70%,#e2e1dd 100%)}
.hero h1{left:62px;top:350px;font-family:"Arimo",sans-serif;font-weight:700;font-size:46px;line-height:53px;color:var(--white);letter-spacing:.5px}
.hero h1 em{font-style:normal;color:var(--gold)}
.btn-contact{left:60px;top:543px;width:131px;height:37px;background:var(--gold);color:var(--white);font-family:"Arimo",sans-serif;font-weight:700;font-size:14px;display:flex;align-items:center;justify-content:center;box-shadow:3px 3px 0 #ddd}

/* feature cards */
.card{top:892px;width:286px;height:98px;background:var(--white);box-shadow:0 2px 10px rgba(0,0,0,.1);display:flex;align-items:center;padding-left:88px;font-size:16px;color:var(--ink);line-height:23px}
.card svg{position:absolute;left:14px;top:26px}
.card::after{content:"";position:absolute;right:0;bottom:0;width:54px;height:4px;background:#bbb}
.card.active::after{left:0;width:100%;background:var(--gold)}

/* mission */
.mission-photo{left:0;top:1065px;width:528px;height:428px;background:linear-gradient(90deg,#b9c0c4 0%,#8f8a86 45%,#d3c7b5 100%);clip-path:polygon(0 0,100% 0,96% 100%,0 100%)}
.eyebrow-line{width:2px;height:34px;background:var(--gold)}
.mission h2{font-family:"Arimo",sans-serif;font-weight:700;font-size:22px;color:var(--ink)}
.lead{font-size:14px;line-height:23px;color:var(--ink)}
.small{font-size:12px;line-height:19.5px;color:var(--muted)}

/* commercial */
.gold-band{left:0;top:1395px;width:1200px;height:615px;background:var(--gold)}
.gold-band-left{left:0;top:1395px;width:510px;height:98px;background:var(--white)}
.commercial h2{left:0;width:1210px;top:1556px;text-align:center;font-family:"Arimo",sans-serif;font-weight:700;font-size:22px;color:var(--white)}
.commercial .intro{left:390px;width:436px;top:1610px;text-align:center;font-size:12px;line-height:19.5px;color:var(--white)}
.node{width:68px;height:68px;border-radius:50%;border:2px solid var(--white);display:flex;align-items:center;justify-content:center}
.node-text{font-size:12px;line-height:19.5px;color:var(--white)}
.hub{left:402px;top:1788px;width:376px;height:376px;border-radius:50%;background:var(--white)}
.grey-band{left:0;top:2010px;width:1200px;height:462px;background:var(--soft)}
.copy{left:61px;top:2168px;width:570px;font-size:12px;line-height:19.5px;color:var(--ink)}
.copy p{margin-bottom:13px}
.doorbell-photo{left:793px;top:2156px;width:407px;height:453px;background:linear-gradient(90deg,#d8dcde 0%,#b9bec1 30%,#8a3d2c 55%,#6d2d20 100%)}
.callbar{left:0;top:2472px;width:825px;height:137px;background:var(--night)}
.call-icon{left:119px;top:2501px;width:76px;height:76px;border-radius:50%;background:var(--gold);display:flex;align-items:center;justify-content:center}
.call-kicker{left:271px;top:2511px;font-size:12px;color:var(--gold)}
.call-title{left:271px;top:2542px;font-size:20px;color:var(--white)}

/* residential */
.res-shadow{left:75px;top:2706px;width:483px;height:436px;background:var(--ink)}
.res-photo{left:60px;top:2692px;width:483px;height:436px;background:radial-gradient(circle at 50% 50%,#3a3a3a 0%,#8b8a88 45%,#d4d2cf 100%)}
.res h2{font-family:"Arimo",sans-serif;font-weight:700;font-size:22px;color:var(--ink)}

/* footer */
.footer{left:0;top:3232px;width:1200px;height:307px;background:var(--gold)}
.footer-brand{left:62px;top:3322px;display:flex;align-items:center;gap:10px;font-weight:600;font-size:20px;color:var(--white);letter-spacing:1px}
.footer-brand i{width:16px;height:16px;border-radius:50%;background:var(--white);display:block}
.socials{left:60px;top:3398px;display:flex;gap:9px}
.socials span{width:34px;height:34px;border-radius:50%;background:var(--white);display:block}
.fcol h3{font-family:"Arimo",sans-serif;font-weight:700;font-size:18px;color:var(--ink);margin-bottom:14px}
.fcol li{list-style:none;font-size:12px;color:var(--white);line-height:30px}
.fcontact{font-size:12px;color:var(--white);line-height:19px;display:flex;gap:16px}
.copyright{left:0;top:3539px;width:1200px;height:39px;background:var(--night);color:var(--white);font-size:12px;display:flex;align-items:center;justify-content:center}
</style>
</head>
<body>

<!-- top bar -->
<div class="abs topbar">
  <span style="left:70px"><svg width="14" height="18" viewBox="0 0 14 18"><path d="M7 1a6 6 0 0 0-6 6c0 4 6 10 6 10s6-6 6-10a6 6 0 0 0-6-6z" fill="none" stroke="#c99a33" stroke-width="1.5"/><circle cx="7" cy="7" r="2" fill="#c99a33"/></svg>Lorem Ipsum is simply dummy text of the printing</span>
  <span style="left:470px"><svg width="20" height="14" viewBox="0 0 20 14"><rect x="1" y="1" width="18" height="12" fill="none" stroke="#c99a33" stroke-width="1.5"/><path d="M1 1l9 7 9-7" fill="none" stroke="#c99a33" stroke-width="1.5"/></svg>&nbsp;&nbsp;info@polarisguard.com</span>
  <span style="left:707px"><svg width="16" height="16" viewBox="0 0 16 16"><path d="M3 1l3 3-2 2c1 2 3 4 5 5l2-2 3 3-2 3C7 15 1 9 1 3z" fill="none" stroke="#c99a33" stroke-width="1.4"/></svg>&nbsp;123 456 7890</span>
</div>

<!-- header -->
<div class="abs brand"><i></i>POLARIS GUARD SOLUTIONS</div>
<nav class="abs nav">
  <a class="active" href="#">Home</a><a href="#">About Us</a><a href="#">Solution</a><a href="#">Resources</a><a href="#">Contact Us</a>
</nav>
<a class="abs quote" href="#">REQUEST A QUOTE</a>

<!-- hero -->
<section class="abs hero" role="img" aria-label="Woman in a home setting pressing a wall-mounted security control panel"></section>
<h1 class="abs hero" style="background:none;height:auto;width:auto;left:62px;top:350px">PROTECT ASSETS AND<br>SECURITY <em>OF YOUR</em><br><em>BUSINESS</em></h1>
<a class="abs btn-contact" href="#">CONTACT US</a>

<!-- feature cards -->
<div class="abs card" style="left:149px">
  <svg width="50" height="46" viewBox="0 0 50 46" fill="none" stroke="#c99a33" stroke-width="2"><rect x="4" y="6" width="28" height="16" rx="2" transform="rotate(15 18 14)"/><circle cx="16" cy="14" r="4"/><path d="M30 24l6 10h10M46 28v12"/></svg>
  Preminum Indoor<br>Cameras</div>
<div class="abs card active" style="left:457px">
  <svg width="50" height="46" viewBox="0 0 50 46" fill="none" stroke="#c99a33" stroke-width="2"><path d="M13 38V24a12 12 0 0 1 24 0v14"/><rect x="8" y="38" width="34" height="5"/><path d="M25 2v6M8 10l4 4M42 10l-4 4M2 24h5M43 24h5"/></svg>
  24/7 Alaram<br>Response</div>
<div class="abs card" style="left:764px">
  <svg width="50" height="46" viewBox="0 0 50 46" fill="none" stroke="#c99a33" stroke-width="2"><rect x="15" y="4" width="20" height="30" rx="3"/><path d="M20 12h10M20 18h10M20 24h10M25 34v8M8 14c-3 4-3 10 0 14M42 14c3 4 3 10 0 14"/></svg>
  Amazing Swecurity<br>Systems</div>

<!-- mission -->
<div class="abs gold-band"></div>
<div class="abs gold-band-left"></div>
<div class="abs mission-photo" role="img" aria-label="Woman in a striped shirt using a wall-mounted security keypad at home"></div>
<div class="abs eyebrow-line" style="left:603px;top:1083px"></div>
<section class="abs mission" style="left:610px;top:1080px;width:400px">
  <h2>Our Mission</h2>
  <p class="lead" style="margin-top:26px">To provide our customers with comprehensive security, audio/video, and automation with top notch customer service. We Ensure Security with Smart Tools.</p>
  <p class="small" style="margin-top:24px;padding-left:4px">The graded security measures from Polaris Guard Solutions ensure the safety of both residential and commercial property. We provide a wide range of Residential and Commercial Security Solutions.</p>
</section>

<!-- commercial -->
<div class="abs grey-band"></div>
<div class="abs hub"></div>
<section class="commercial">
  <div class="abs eyebrow-line" style="left:482px;top:1556px;height:30px;background:var(--white)"></div>
  <h2 class="abs">Commercial Solutions</h2>
  <p class="abs intro">CCTV cameras equipped with facial recognition technologies enable the technology to identify the offenders.</p>
  <svg class="abs" style="left:0;top:1660px" width="1200" height="340" fill="none" stroke="#ffffff" stroke-width="1.2" stroke-dasharray="6 5">
    <path d="M592 62v110"/><path d="M410 138l42 44"/><path d="M773 138l-42 44"/><path d="M320 301h82"/><path d="M778 301h95"/>
  </svg>
  <div class="abs node" style="left:558px;top:1655px"><svg width="30" height="36" viewBox="0 0 30 36" fill="none" stroke="#fff" stroke-width="1.6"><path d="M3 4h24v6H3z"/><path d="M5 10c0 14 20 14 20 0"/><circle cx="15" cy="17" r="5"/><circle cx="15" cy="17" r="2"/></svg></div>
  <div class="abs node" style="left:352px;top:1738px"><svg width="30" height="36" viewBox="0 0 30 36" fill="none" stroke="#fff" stroke-width="1.6"><rect x="8" y="4" width="14" height="22" rx="2"/><path d="M11 10h8M11 15h8M11 20h8M15 26v6M3 10c-2 4-2 8 0 12M27 10c2 4 2 8 0 12"/></svg></div>
  <div class="abs node" style="left:762px;top:1738px"><svg width="34" height="30" viewBox="0 0 34 30" fill="none" stroke="#fff" stroke-width="1.6"><rect x="2" y="4" width="18" height="11" transform="rotate(15 11 9)"/><circle cx="10" cy="10" r="3"/><path d="M20 16l4 7h8M32 19v8"/></svg></div>
  <div class="abs node" style="left:251px;top:1927px"><svg width="32" height="30" viewBox="0 0 32 30" fill="none" stroke="#fff" stroke-width="1.6"><rect x="3" y="4" width="26" height="18"/><rect x="9" y="9" width="10" height="7"/><path d="M19 11l5-3v9l-5-3M10 26h12"/></svg></div>
  <div class="abs node" style="left:873px;top:1925px"><svg width="28" height="32" viewBox="0 0 28 32" fill="none" stroke="#fff" stroke-width="1.6"><rect x="3" y="3" width="22" height="26"/><rect x="7" y="7" width="14" height="7"/><path d="M8 19h2M13 19h2M18 19h2M8 24h2M13 24h2M18 24h2"/></svg></div>
  <p class="abs node-text" style="left:174px;top:1764px">Burglar Alarms &amp; Detectors</p>
  <p class="abs node-text" style="left:853px;top:1742px;width:280px">Monitoring of alarms and video recordings 24 hours a day, seven days a week. Addressing all the incidents with an urgent response.</p>
  <p class="abs node-text" style="left:60px;top:1939px;width:180px;text-align:right">Audio &amp; Video Solutions for your commercial property</p>
  <p class="abs node-text" style="left:958px;top:1921px;width:170px">Alarm systems and cameras precisely installed so that more of your property is tracked.</p>
</section>

<div class="abs copy">
  <p>We will help secure your company outside of the realm of conventional monitoring technologies. Indeed, we take a customised and comprehensive approach to defence.</p>
  <p>Flooding, smoke, power outages, temperature fluctuations, and other factors will all be tracked. So, you can take prompt steps before you experience damage.</p>
  <p>But, it all comes down to internal and external security measures.</p>
  <p>Flooding, smoke, power outages, temperature fluctuations, and other factors will all be tracked. So, you can take prompt steps before you experience damage.</p>
  <p>We can combine low-light cameras, smoke and temperature monitoring, noise control, and physical surveillance into a 24/7 commercial security solution. Thus, you can focus on running your business with utmost safety</p>
</div>
<div class="abs doorbell-photo" role="img" aria-label="Finger pressing a smart video doorbell mounted beside a red brick wall"></div>

<!-- call bar -->
<div class="abs callbar"></div>
<div class="abs call-icon"><svg width="38" height="38" viewBox="0 0 16 16"><path d="M3 1l3 3-2 2c1 2 3 4 5 5l2-2 3 3-2 3C7 15 1 9 1 3z" fill="none" stroke="#fff" stroke-width="1.2"/></svg></div>
<p class="abs call-kicker">24 Hours Services Available</p>
<p class="abs call-title">Call Our Investogator Now To Solve Your Problem</p>

<!-- residential -->
<div class="abs res-shadow"></div>
<div class="abs res-photo" role="img" aria-label="Hands holding a tablet showing a grid of home security camera feeds"></div>
<div class="abs eyebrow-line" style="left:632px;top:2758px;height:30px"></div>
<section class="abs res" style="left:632px;top:2754px;width:390px">
  <h2>Residential Security Solutions</h2>
  <p class="lead" style="margin-top:16px">Consider a home surveillance device that would do more for you and your family than you ever imagined.</p>
  <p class="small" style="margin-top:14px">Polaris Guard Solutions is your trustable security provider. Also, as certified professionals carry out the installation, you have everything under control. Your home is being securely watched from various points, with cameras capable of tracking any intruder's path. Specifically, we offer Residential Intrusion Detection Security Systems, Residential Alarm, Residential Network Wi-Fi, CCTVs and residential home automation.</p>
</section>

<!-- footer -->
<footer class="abs footer"></footer>
<div class="abs footer-brand"><i></i>POLARIS GUARD</div>
<div class="abs socials"><span></span><span></span><span></span></div>
<div class="abs fcol" style="left:337px;top:3307px"><h3>Site Map</h3><ul><li>- Home</li><li>- About Us</li><li>- Solution</li><li>- Resources</li><li>- Contact Us</li></ul></div>
<div class="abs fcol" style="left:613px;top:3307px"><h3>Support</h3><ul><li>- Forum Support</li><li>- Help &amp; FAQ</li><li>- Contact Us</li><li>- Cookies Policy</li></ul></div>
<div class="abs fcol" style="left:889px;top:3307px"><h3>Contact Us</h3></div>
<div class="abs fcontact" style="left:889px;top:3347px"><svg width="16" height="22" viewBox="0 0 14 18"><path d="M7 1a6 6 0 0 0-6 6c0 4 6 10 6 10s6-6 6-10a6 6 0 0 0-6-6z" fill="none" stroke="#111" stroke-width="1.5"/><circle cx="7" cy="7" r="2" fill="#111"/></svg><span style="width:200px">Lorem Ipsum is simply dummy text of the printing</span></div>
<div class="abs fcontact" style="left:889px;top:3407px"><svg width="16" height="16" viewBox="0 0 16 16"><path d="M3 1l3 3-2 2c1 2 3 4 5 5l2-2 3 3-2 3C7 15 1 9 1 3z" fill="#111"/></svg><span>123 456 7890</span></div>
<div class="abs fcontact" style="left:889px;top:3460px"><svg width="20" height="14" viewBox="0 0 20 14"><rect x="1" y="1" width="18" height="12" fill="#111"/><path d="M1 1l9 7 9-7" fill="none" stroke="#c99a33" stroke-width="1.2"/></svg><span>info@polarisguard.com</span></div>
<div class="abs copyright">2021 ©POLARIS GUARD -All Right Reserved.</div>

</body>
</html>
```